RM BIZ CARDS

Hi,

Is it possible to see a one sided version (with logo and info) as well as a two-sided version (front side w/logo and back side with info)?
How do we choose card stock and finish once we approve a design?

We would like the following info included:

Peter Lowell
Rosfeld Talent Media
4127 Marwick Lane, Suite 300
Los Angeles, CA 90041
(323) 555-0148
peter@rosfeldtalentmedia.example

```html
<!DOCTYPE html>
<html lang="en">
<head>
<meta charset="utf-8">
<title>Rosfeld Talent Media – Business Cards</title>
<link rel="stylesheet" href="https://fonts.googleapis.com/css2?family=Cabin:wght@400;600&display=swap">
<style>
  :root {
    --page-bg: #e4e4e4;
    --card-paper: #f3f3f2;
    --accent-maroon: #7f4a4b;
    --ink-black: #141414;
    --ink-body: #2e2e2e;
    --icon-light: #ffffff;
  }
  html, body {
    margin: 0;
    padding: 0;
    width: 1200px;
    height: 1000px;
    overflow: hidden;
    background: var(--page-bg);
    font-family: "Cabin", "Gill Sans", sans-serif;
  }
  .canvas {
    position: relative;
    width: 1200px;
    height: 1000px;
  }
  .card {
    position: absolute;
    left: 250px;
    width: 692px;
    height: 414px;
    background: var(--card-paper);
    box-shadow: 0 1px 3px rgba(0,0,0,0.12);
    overflow: hidden;
  }
  .card--front { top: 64px; }
  .card--back { top: 500px; }

  .wordmark {
    position: absolute;
    margin: 0;
    font-weight: 400;
    color: var(--ink-black);
    text-transform: uppercase;
    white-space: nowrap;
    line-height: 1;
  }
  .card--front .wordmark {
    left: 0;
    right: 0;
    top: 266px;
    text-align: center;
    font-size: 40px;
    letter-spacing: 5px;
  }
  .card--back .wordmark {
    right: 46px;
    top: 152px;
    font-size: 26px;
    letter-spacing: 3px;
  }

  .side-band {
    position: absolute;
    left: 0;
    top: 0;
    width: 70px;
    height: 100%;
    background: var(--accent-maroon);
  }

  .contact {
    position: absolute;
    left: 78px;
    top: 252px;
  }
  .contact__name {
    margin: 0 0 16px;
    font-size: 20px;
    font-weight: 600;
    letter-spacing: 0.5px;
    text-transform: uppercase;
    color: var(--accent-maroon);
    line-height: 1;
  }
  .contact__company {
    margin: 0 0 4px;
    font-size: 17px;
    font-weight: 600;
    color: var(--ink-black);
    line-height: 20px;
  }
  .contact__line {
    margin: 0;
    font-size: 15px;
    color: var(--ink-body);
    line-height: 20px;
  }

  .contact-icon {
    position: absolute;
    left: 52px;
    width: 13px;
    height: 13px;
  }
  .contact-icon--pin { top: 311px; }
  .contact-icon--phone { top: 353px; }
  .contact-icon--mail { top: 374px; }
</style>
</head>
<body>
<main class="canvas">

  <section class="card card--front" aria-label="Card front">
    <h1 class="wordmark">Rosfeld Talent</h1>
  </section>

  <section class="card card--back" aria-label="Card back">
    <div class="side-band"></div>

    <h2 class="wordmark">Rosfeld Talent</h2>

    <svg class="contact-icon contact-icon--pin" viewBox="0 0 12 12" aria-hidden="true">
      <path d="M6 0.5a4 4 0 0 0-4 4c0 3 4 7 4 7s4-4 4-7a4 4 0 0 0-4-4z" fill="var(--icon-light)"/>
      <circle cx="6" cy="4.5" r="1.5" fill="var(--accent-maroon)"/>
    </svg>
    <svg class="contact-icon contact-icon--phone" viewBox="0 0 12 12" aria-hidden="true">
      <path d="M2.5 1l2 2.2-1.1 1.4a7 7 0 0 0 4 4l1.4-1.1L11 9.5 9.6 11C5 11 1 7 1 2.4z" fill="var(--icon-light)"/>
    </svg>
    <svg class="contact-icon contact-icon--mail" viewBox="0 0 12 12" aria-hidden="true">
      <rect x="0.5" y="2.5" width="11" height="8" fill="var(--icon-light)"/>
      <path d="M0.8 2.8L6 7l5.2-4.2" fill="none" stroke="var(--accent-maroon)" stroke-width="1"/>
    </svg>

    <div class="contact">
      <p class="contact__name">Peter Lowell</p>
      <p class="contact__company">Rosfeld Talent Media</p>
      <p class="contact__line">4127 Marwick Lane, Suite 300</p>
      <p class="contact__line">Los Angeles, CA 90041</p>
      <p class="contact__line">(323) 555-0148</p>
      <p class="contact__line">peter@rosfeldtalentmedia.example</p>
    </div>
  </section>

</main>
</body>
</html>
```